Platelet Rich Plasma (PRP) Flyer

Hi,

Looking to spruce up our Platelet Rich Plasma Flyer (see power point attachment). I also included previous flyers as examples on the design style we are looking for.

Quorum is our official font of our logo.
Attached is our logo in EPS format.
Please use the current photos in the power point. If you include photos, please make sure the stock image is free.

Files must be under 5MB. JPEG, PNG, PDF, .ai

Thank you,
Marcus

Target Market(s)

Patients

Industry/Entity Type

Healthcare

Font styles to use
Other font styles liked:
• Quorum

Requirements
Must have
• Emphasis on Platelet Rich Plasma Therapy when they pick up the flyer. The price of $199. FSA/HSA Eligible. The different treatment areas. The three addresses. Best of the best logo can be very small, not as important.
Nice to have
• One or two pictures. Less is more
Should not have
• Long paragraphs, multiple sentences.

```html
<!DOCTYPE html>
<html lang="en">
<head>
<meta charset="utf-8">
<title>Platelet Rich Plasma Therapy Flyer</title>
<link href="https://fonts.googleapis.com/css2?family=Bree+Serif&family=Signika:wght@400;600;700&display=swap" rel="stylesheet">
<style>
  :root {
    --page-bg: #d9d9d9;
    --paper: #ececec;
    --charcoal: #333333;
    --orange: #f2804a;
    --teal: #52c3a6;
    --navy: #2d4b62;
    --photo-lab: #c9c2b8;
    --ink: #2b2b2b;
    --white: #ffffff;
    --ring: #e6e6e6;
  }
  * { box-sizing: border-box; margin: 0; padding: 0; }
  html, body { width: 1027px; height: 1200px; overflow: hidden; background: var(--page-bg); }
  body { font-family: "Signika", sans-serif; }
  .flyer {
    position: absolute; left: 53px; top: 5px;
    width: 920px; height: 1190px;
    background: var(--paper); overflow: hidden;
  }
  .shapes { position: absolute; inset: 0; }
  .brand { position: absolute; left: 60px; top: 62px; display: flex; align-items: center; gap: 14px; }
  .brand-dot { width: 22px; height: 22px; border-radius: 50%; background: var(--teal); }
  .brand-name { font-weight: 700; font-size: 34px; line-height: 1; color: var(--orange); letter-spacing: .5px; }
  .brand-url { position: absolute; left: 96px; top: 106px; font-weight: 600; font-size: 14px; color: var(--orange); letter-spacing: .4px; }
  .headline { position: absolute; left: 80px; top: 300px; font-family: "Bree Serif", serif; font-size: 52px; line-height: 60px; color: var(--ink); font-weight: 400; }
  .price-badge { position: absolute; left: 460px; top: 322px; width: 200px; text-align: center; color: var(--white); }
  .price-label { font-family: "Bree Serif", serif; font-size: 22px; line-height: 26px; }
  .price-amount { font-weight: 700; font-size: 34px; line-height: 42px; }
  .price-unit { font-family: "Bree Serif", serif; font-size: 22px; line-height: 24px; }
  .price-note { font-weight: 600; font-size: 15px; line-height: 22px; color: var(--ink); }
  .intro { position: absolute; left: 90px; width: 420px; font-size: 18px; line-height: 25px; color: var(--white); }
  .intro-1 { top: 520px; }
  .intro-2 { top: 630px; }
  .treating { position: absolute; left: 110px; top: 770px; color: var(--white); font-weight: 700; font-size: 24px; line-height: 33px; }
  .services { position: absolute; right: 80px; top: 852px; text-align: right; color: var(--white); font-size: 18px; line-height: 25px; font-weight: 600; }
  .phone { display: flex; align-items: center; justify-content: flex-end; gap: 8px; font-size: 27px; font-weight: 700; margin-top: 6px; }
  .icon-badge { width: 24px; height: 24px; flex: none; border-radius: 50%; background: var(--orange); display: inline-flex; align-items: center; justify-content: center; }
  .banner { position: absolute; left: 0; top: 990px; width: 100%; height: 82px; background: var(--teal); text-align: center; color: var(--ink); font-weight: 600; font-size: 26px; line-height: 33px; padding-top: 9px; }
  .offices { position: absolute; left: 0; top: 1088px; width: 100%; display: flex; justify-content: space-around; padding: 0 40px; }
  .office { display: flex; gap: 8px; color: var(--white); font-size: 16px; line-height: 21px; }
  .office-name { color: var(--teal); font-weight: 600; font-size: 19px; line-height: 24px; }
</style>
</head>
<body>
<div class="flyer">
  <svg class="shapes" width="920" height="1190" viewBox="0 0 920 1190">
    <rect x="0" y="520" width="920" height="670" fill="var(--charcoal)"/>
    <path d="M520 0 H920 V560 H700 A290 290 0 0 1 520 0 Z" fill="var(--navy)" role="img" aria-label="Photo: runner holding a painful knee and leg"/>
    <circle cx="300" cy="620" r="408" fill="var(--ring)"/>
    <circle cx="300" cy="620" r="400" fill="var(--orange)"/>
    <circle cx="770" cy="640" r="178" fill="var(--ring)"/>
    <circle cx="770" cy="640" r="170" fill="var(--photo-lab)" role="img" aria-label="Photo: gloved hands placing blood tubes into a centrifuge"/>
    <circle cx="560" cy="395" r="118" fill="var(--ring)"/>
    <circle cx="560" cy="395" r="110" fill="var(--teal)"/>
  </svg>

  <div class="brand"><span class="brand-dot"></span><span class="brand-name">HARBORVIEW FOOT &amp; ANKLE</span></div>
  <div class="brand-url">STEPWELLCLINIC.COM</div>

  <h1 class="headline">Platelet<br>Rich Plasma<br>Therapy (PRP)</h1>

  <div class="price-badge">
    <div class="price-label">SELF<br>PAY PRICE:</div>
    <div class="price-amount">$199 PER</div>
    <div class="price-unit">treatment</div>
    <div class="price-note">FSA/HSA Eligible</div>
  </div>

  <p class="intro intro-1">PRP uses platelets from your own blood, rich in proteins that speed tissue repair and new cell growth.</p>
  <p class="intro intro-2">Injected into damaged tissue, it helps your body heal. A consultation is required to qualify.</p>

  <div class="treating">TREATING:<br>Plantar Fasciitis |<br>Achilles Tendonitis |<br>Tendon &amp; Ligament Injuries</div>

  <div class="services">
    Podiatry | Foot &amp; Ankle Surgery<br>Sports Medicine | Wound Care
    <div class="phone">
      <span class="icon-badge"><svg width="14" height="14" viewBox="0 0 24 24"><path d="M6.6 10.8a15 15 0 0 0 6.6 6.6l2.2-2.2c.3-.3.7-.4 1-.2 1.1.4 2.3.6 3.6.6.6 0 1 .4 1 1V20c0 .6-.4 1-1 1C10.6 21 3 13.4 3 4c0-.6.4-1 1-1h3.5c.6 0 1 .4 1 1 0 1.3.2 2.5.6 3.6.1.3 0 .7-.2 1z" fill="#fff"/></svg></span>
      (555) 214 - 0370
    </div>
  </div>

  <div class="banner">Same Day | Emergency | Saturday Appointments<br>Our Doctors are on call at the MVH ER 24/7</div>

  <div class="offices">
    <div class="office">
      <span class="icon-badge"><svg width="14" height="14" viewBox="0 0 24 24"><path d="M12 2a7 7 0 0 0-7 7c0 5 7 13 7 13s7-8 7-13a7 7 0 0 0-7-7zm0 9.5A2.5 2.5 0 1 1 12 6.5a2.5 2.5 0 0 1 0 5z" fill="#fff"/></svg></span>
      <div><div class="office-name">Harborview Office</div>218 Linden Park Dr. Ste. 140<br>Harborview, MD 21790</div>
    </div>
    <div class="office">
      <span class="icon-badge"><svg width="14" height="14" viewBox="0 0 24 24"><path d="M12 2a7 7 0 0 0-7 7c0 5 7 13 7 13s7-8 7-13a7 7 0 0 0-7-7zm0 9.5A2.5 2.5 0 1 1 12 6.5a2.5 2.5 0 0 1 0 5z" fill="#fff"/></svg></span>
      <div><div class="office-name">Millbrook Office</div>5120 Orchard Ridge Blvd. Ste. 305<br>Millbrook, MD 21795</div>
    </div>
    <div class="office">
      <span class="icon-badge"><svg width="14" height="14" viewBox="0 0 24 24"><path d="M12 2a7 7 0 0 0-7 7c0 5 7 13 7 13s7-8 7-13a7 7 0 0 0-7-7zm0 9.5A2.5 2.5 0 1 1 12 6.5a2.5 2.5 0 0 1 0 5z" fill="#fff"/></svg></span>
      <div><div class="office-name">Cedar Falls Office</div>77 Wellness Way<br>Cedar Falls, WV 25490</div>
    </div>
  </div>
</div>
</body>
</html>
```